依頼概要
当社はガソリンスタンドを6店舗運営している会社です。
車検獲得のための予約促進及びリピーターへのフォロー、車販売にもつながるDMデザインの提案をお願いいたします。

車検獲得に向けた2年間のフローの中で数回に分けてDMを発送予定しています。
既存使用しているDMもある為、今回は新規作成分の4種類のDMになります。

デザインを採用させていただいた方には改めて詳細の打ち合わせをしたいと思います。また、当社作成物の今後の依頼もさせて頂く場合もあります。

よろしくお願いいたします。

資料として当社車検フロー、DM内容、参考資料を添付いたします
車検価格表を追加しました
依頼金額を増額させて頂きました。
現在使用中のDMを参考まで
依頼金額を59400円に変更して、延長しました。
数多くの提案を頂きたい為、延長させていただきます。
はがきサイズにとらわれず、情報量を増やしていただいても結構です。

明確な特典アピール

今回はご提案頂きありがとうございました

```html
<!DOCTYPE html>
<html lang="ja">
<head>
<meta charset="utf-8">
<title>ハッピー車検 限定特典</title>
<link href="https://fonts.googleapis.com/css2?family=M+PLUS+Rounded+1c:wght@500;800;900&family=Noto+Sans+JP:wght@500;700;900&family=Playfair+Display:wght@700&display=swap" rel="stylesheet">
<style>
:root{
  --orange:#f29a1f;
  --orange-deep:#ea7a10;
  --red:#e5201c;
  --navy:#1c2f5e;
  --gold:#e9c66b;
  --white:#ffffff;
  --ink:#1d2233;
  --cream:#fff7ea;
}
*{margin:0;padding:0;box-sizing:border-box}
html,body{width:811px;height:1200px;overflow:hidden}
body{background:var(--orange);font-family:"Noto Sans JP",sans-serif;color:var(--ink);position:relative}
.abs{position:absolute}
.title{left:30px;top:4px;font-family:"M PLUS Rounded 1c",sans-serif;font-weight:900;font-size:66px;color:var(--white);letter-spacing:2px;line-height:72px}
.mascot{left:540px;top:0;width:260px;height:240px;border-radius:50%;background:radial-gradient(circle at 50% 45%,#f6d7b0,#d9a26b 70%,#c98d55);}
.panel{left:0;top:78px;width:811px;height:330px;background:var(--white)}
.offer-box{left:27px;top:82px;width:515px;height:78px;background:var(--orange);border-radius:10px;color:var(--white);font-weight:900;padding:8px 14px;font-size:22px;line-height:30px}
.offer-box .big{font-size:44px;line-height:44px;color:var(--white);position:absolute;right:14px;top:20px;text-shadow:2px 2px 0 var(--red)}
.service{left:27px;top:170px;width:515px;height:48px;background:var(--orange-deep);border-radius:8px;color:var(--white);font-weight:900;font-size:32px;line-height:48px;text-align:center}
.service small{font-size:22px;margin:0 6px}
.free{left:30px;top:215px;font-family:"M PLUS Rounded 1c",sans-serif;font-weight:900;font-size:160px;line-height:180px;color:var(--red);letter-spacing:4px;-webkit-text-stroke:4px var(--white);paint-order:stroke}
.engine{left:600px;top:256px;width:185px;height:150px;border-radius:8px;background:linear-gradient(135deg,#5b5f66,#2d3036 60%,#9aa0a8)}
.visit{left:600px;top:218px;color:var(--red);font-weight:900;font-size:17px;line-height:20px;text-align:right;width:185px}
.more{left:30px;top:412px;color:var(--white);font-weight:900;font-size:22px}
.members{left:27px;top:440px;width:757px;height:56px;background:var(--navy);border-radius:8px;color:var(--gold);font-family:"Playfair Display",serif;font-weight:700;font-size:42px;line-height:56px;padding-left:24px}
.members span{font-family:"Noto Sans JP",sans-serif;font-weight:900;font-size:36px;color:var(--white)}
.docking{left:27px;top:506px;width:757px;height:236px;background:var(--white);border-radius:10px}
.dock-text{left:54px;top:522px;font-weight:900;font-size:34px;line-height:46px;color:var(--navy)}
.dock-text em{font-style:normal;color:var(--red)}
.rate-label{left:470px;top:530px;font-weight:900;font-size:34px;line-height:40px;color:var(--navy)}
.rate-fuel{left:590px;top:520px;font-size:15px;font-weight:700;color:var(--white);background:var(--red);border-radius:4px;padding:1px 8px}
.rate{left:580px;top:540px;font-family:"M PLUS Rounded 1c",sans-serif;font-weight:900;font-size:110px;line-height:120px;color:var(--red)}
.rate small{font-size:40px}
.note{left:54px;top:680px;font-size:13px;line-height:22px;color:var(--ink);width:710px}
.items{left:27px;top:750px;width:757px;height:42px;background:var(--navy);border-radius:21px;color:var(--white);font-weight:900;font-size:24px;line-height:42px;display:flex;justify-content:space-around}
.items span::before{content:"●";color:var(--orange);margin-right:4px}
.tier{top:802px;width:248px;height:390px}
.tier .need{font-weight:900;font-size:22px;line-height:30px;color:var(--ink)}
.tier .need b{color:var(--white);background:var(--red);border-radius:50%;display:inline-block;width:40px;height:40px;text-align:center;line-height:40px;font-size:28px;margin-right:6px;float:left}
.card{position:absolute;left:10px;top:88px;width:228px;height:174px;border-radius:12px}
.bronze{background:linear-gradient(135deg,#8a5a3a,#d69b70 50%,#7a4c2e)}
.silver{background:linear-gradient(135deg,#8c9096,#eef0f2 50%,#8a8e94)}
.goldc{background:linear-gradient(135deg,#a98031,#f5dc8c 50%,#9c7425)}
.deal{position:absolute;left:0;top:292px;width:248px;height:92px;background:var(--white);border-radius:10px;display:flex;align-items:center;padding:0 8px}
.badge{width:62px;height:62px;border-radius:50%;color:var(--white);font-weight:900;font-size:13px;line-height:16px;display:flex;align-items:center;justify-content:center;text-align:center;flex:none}
.deal .amt{font-family:"M PLUS Rounded 1c",sans-serif;font-weight:900;color:var(--red);font-size:48px;margin-left:8px;line-height:60px}
.deal .amt small{font-size:22px;color:var(--ink)}
</style>
</head>
<body>
<div class="abs title">ハッピー車検</div>
<div class="abs mascot" role="img" aria-label="車検キャラクターのイラスト"></div>
<div class="abs panel"></div>
<div class="abs offer-box">車検を予約・実施<br>していただいた方<span class="big">限定特典!!</span></div>
<div class="abs service">オイル交換<small>または</small>エンジン洗浄</div>
<div class="abs free">無料!</div>
<div class="abs visit">お気軽に<br>お越しください</div>
<div class="abs engine" role="img" aria-label="エンジン洗浄作業の写真"></div>

<div class="abs more">さらにお得な</div>
<div class="abs members">Premium Members<span>登場!</span></div>
<div class="abs docking"></div>
<div class="abs dock-text">ガソリンスタンドと<br>ご家庭の<em>プロパンガス</em><br>がドッキング!</div>
<div class="abs rate-label">最大<br>割引</div>
<div class="abs rate-fuel">ガソリン｜軽油</div>
<div class="abs rate">15<small>円/ℓ</small></div>
<div class="abs note">※当社グループで下記の商品を複数ご利用のお客様に燃料油価格で還元します。<br>※当社でガスをご契約の方が対象となります（新規切替の申込者も含みます）</div>
<div class="abs items"><span>ガスコンロ</span><span>ガス給湯器</span><span>ガスファンヒーター</span><span>車検</span></div>

<div class="abs tier" style="left:20px">
  <div class="need"><b>2</b>アイテム該当の<br>お役様には…</div>
  <div class="card bronze" role="img" aria-label="Sunrise Group ブロンズ会員カード"></div>
  <div class="deal"><div class="badge" style="background:#a8693f">ブロンズ<br>会員</div><div class="amt">5<small>円/ℓ Off</small></div></div>
</div>
<div class="abs tier" style="left:281px">
  <div class="need"><b>3</b>アイテム該当の<br>お役様には…</div>
  <div class="card silver" role="img" aria-label="Sunrise Group シルバー会員カード"></div>
  <div class="deal"><div class="badge" style="background:#8e949b">シルバー<br>会員</div><div class="amt">10<small>円/ℓ Off</small></div></div>
</div>
<div class="abs tier" style="left:542px">
  <div class="need"><b>4</b>アイテム該当の<br>お役様には…</div>
  <div class="card goldc" role="img" aria-label="Sunrise Group ゴールド会員カード"></div>
  <div class="deal"><div class="badge" style="background:#c39a3a">ゴールド<br>会員</div><div class="amt">15<small>円/ℓ Off</small></div></div>
</div>
</body>
</html>
```